Bright Acorn day Nursery flyer

I need a great flyer to attract new parents. Bright Acorn Is a fantastic, warm and homely nursery in Westmere road SE6 London. We offer many things that other nurseries don't offer such as Spanish, Yoga, Music, Cooking classes and Makaton. We also have an amazing system called KINDTRAK that allows parents to get alerts on the KINDTRAK app about their children daily activities and even developmental reports. Parents are able to share with the nursery great moments and put pictures and videos through the app. We also offer the parent camera, an extremely safe system that allows parents to log in and see their children whilst they are engaged in exciting activities.
Full details of Nursery
87 Westmere road
SE6 4QP
02084417260
www.brightacornhollis.co.uk
facebook page
brightacorndaynursery@brightacornhollis.co.uk
Updates

double sided or mini brochure type

Hi Please keep it simple and clean I feel the designs are a good attempt thank you but they are very busy and I just want to add important points a lot of the designs have too many colours, too much text etc Thank you!

https://www.facebook.com/brightacornhollis.co.uk/

Target Market(s)

parents of children 0-5

Industry/Entity Type

Childcare

Colors

Designer to choose colors to be used in the design.

Requirements
Must have
• colour and pictures but clean design

```html
<!DOCTYPE html>
<html lang="en">
<head>
<meta charset="utf-8">
<title>Bright Acorn Day Nursery – Brochure</title>
<link href="https://fonts.googleapis.com/css2?family=Montserrat:wght@300;400;600&family=Open+Sans:wght@400;600&display=swap" rel="stylesheet">
<style>
  :root {
    --backdrop: #9a9a9a;
    --paper: #ffffff;
    --brand-blue: #3b43a6;
    --ink: #2f2f2f;
    --ink-soft: #555555;
    --photo-warm: #b98a5a;
    --photo-green: #8ccf3e;
    --photo-dark: #3d3a35;
  }
  * { box-sizing: border-box; margin: 0; padding: 0; }
  html, body { width: 1200px; height: 804px; overflow: hidden; }
  body {
    background: var(--backdrop);
    font-family: "Open Sans", Arial, sans-serif;
    color: var(--ink);
  }
  .brochure {
    position: absolute;
    left: 192px; top: 22px;
    display: flex; gap: 16px;
  }
  .panel {
    position: relative;
    width: 400px; height: 760px;
    background: var(--paper);
    overflow: hidden;
    box-shadow: 0 6px 18px rgba(0,0,0,0.18);
  }
  /* About panel */
  .hero { position: absolute; left: 0; top: 0; width: 400px; height: 270px; display: block; }
  .about {
    position: absolute; left: 36px; right: 36px; top: 262px;
  }
  .panel-title {
    font-family: "Montserrat", Arial, sans-serif;
    font-weight: 300;
    font-size: 26px;
    letter-spacing: 1px;
    line-height: 1.2;
    color: var(--ink);
    margin-bottom: 20px;
  }
  .lead {
    font-size: 15px;
    line-height: 1.45;
    color: var(--ink);
    margin-bottom: 20px;
  }
  .body-copy {
    font-size: 9.6px;
    line-height: 1.55;
    color: var(--ink-soft);
    margin-bottom: 12px;
  }
  /* Services panel */
  .services { position: absolute; left: 40px; right: 36px; top: 44px; }
  .services .panel-title { margin-bottom: 24px; }
  .service { margin-bottom: 30px; }
  .service-title {
    font-family: "Montserrat", Arial, sans-serif;
    font-weight: 600;
    font-size: 12.5px;
    letter-spacing: 0.6px;
    margin-bottom: 10px;
  }
  .service .body-copy { padding-left: 16px; margin-bottom: 10px; }
  .footer-band {
    position: absolute; left: 0; right: 0; bottom: 0; height: 22px;
    background: var(--brand-blue);
  }
</style>
</head>
<body>
<main class="brochure">
  <section class="panel panel-about">
    <svg class="hero" viewBox="0 0 400 270">
      <defs>
        <linearGradient id="heroTone" x1="0" y1="0" x2="1" y2="1">
          <stop offset="0" stop-color="#3d3a35"/>
          <stop offset="0.45" stop-color="#b98a5a"/>
          <stop offset="1" stop-color="#8ccf3e"/>
        </linearGradient>
      </defs>
      <rect role="img" aria-label="Photo of a young girl concentrating on an activity in a colourful playroom" x="0" y="0" width="400" height="270" fill="url(#heroTone)"/>
      <path d="M40 0 H400 V60 C330 62 300 34 250 26 C180 16 110 18 40 0 Z" fill="#3b43a6"/>
      <path d="M0 222 C80 196 220 186 300 196 C350 204 380 222 400 236 V270 H0 Z" fill="#ffffff"/>
    </svg>
    <div class="about">
      <h2 class="panel-title">ABOUT US</h2>
      <p class="lead">We are a privately owned, vibrant nursery offering your child a caring, family environment within the popular Hollis Estate. We offer high quality day care for all children from 3 months to 5 years, treating each child as a treasured individual.</p>
      <p class="body-copy">At Bright Acorn we know that choosing the best nursery for your child is vital but it can seem very daunting. You need to be absolutely sure you have made the right decision to give you peace of mind.</p>
      <p class="body-copy">We have established this nursery very much from a parents’ perspective. We have a passion for delivering high quality care, love and fun learning opportunities. This is at the heart of Bright Acorn. We provide a loving and nurturing family environment enabling children to experience such homely activities as they would at home both within the setting and also in the local community. We promote confident, happy, caring, collaborative learners. We also aspire for the children and our staff to achieve highly as they develop and grow in all aspects.</p>
    </div>
  </section>

  <section class="panel panel-services">
    <div class="services">
      <h2 class="panel-title">EXTRA SERVICES</h2>
      <article class="service">
        <h3 class="service-title">PARENT CAMERA</h3>
        <p class="body-copy">As part of our philosophy of family friendly childcare, we are very excited about this system which is rarely found in day nurseries.</p>
        <p class="body-copy">This is a CCTV and SECURE Webcam facility which allows parents to view live images of their children in the nursery during the day over the internet. You can “drop in” at any time, helping to reassure you by letting you see for yourself how happy your child is at Bright Acorn, and giving you the opportunity to be more involved in your child’s daily activities.</p>
        <p class="body-copy">The Parent Camera is video only, so no sound is heard. It is designed to allow parents to see their children from anywhere, be it at work, at home or on a business trip overseas. There is no special software required, just an internet connection. Viewing on mobile devices is also possible.</p>
        <p class="body-copy">Security is the highest priority within the system, the same technologies and processes as on-line banking and military organisations are employed. Image encryption technology ensures the images can not be “eavesdropped”.</p>
      </article>
      <article class="service">
        <h3 class="service-title">KINDTRAK PARENT</h3>
        <p class="body-copy">KindTrak Parent enables parents to understand their child’s development on a more regular and real-time basis, increasing their involvement in the activities at the nursery.</p>
        <p class="body-copy">Parents can access their child’s learning journey, daily diaries and reports on their mobile devices and computers/laptops through secure logins. Automatic email and push notifications can be sent as soon as a new observations and comments are added on the child’s profile.</p>
        <p class="body-copy">KindTrak Parent also makes it possible for parents to contribute their observations and activities from home, making the learning journey even more comprehensive and enabling a 360 degree view of the child’s development in its early years. Nursery staff can review parent observations, link them to EYFS assessments, add their own comments and publish these to the child’s learning journey.</p>
      </article>
    </div>
    <div class="footer-band"></div>
  </section>
</main>
</body>
</html>
```